Herbal tea shop web designing - Leafwell

We need a business-charity purpose online shop selling premium herbal teas with a tagline "Healthy with a heart" where all the raw materials are being purchased from Indonesian local farmers in order to give them sustainable employment. Every 20% from the total amount of the customer's purchase from our website always goes back to their communities to help build better sanitation, education or whatever they need. We need page to blog too and another page for customers to interact and share their thought. we expect an eye catching simple earthy (maybe a bit rustic) design with some brush lettering font in some parts. Thank you.

Target Market(s)

-Tea Lovers
-Anyone with body weight issues or any health issues in general

Industry/Entity Type

Home Health Care

Number of Pages Required

5+ page

Font styles to use
Other font styles liked:
• brush lettering font in some parts

Requirements
Must have
• - Brush lettering font
• -Simple, a bit rustic design with some nice watercolor touch
• -Blogging Page
• -catchy yet fancy and elegant E-commerce page
Nice to have
• Well, I will let the designers use their skills and imaginations to the fullest.

```html
<!DOCTYPE html>
<html lang="en">
<head>
<meta charset="utf-8">
<title>Leafwell — Healthy with a heart</title>
<link rel="stylesheet" href="https://fonts.googleapis.com/css2?family=Kaushan+Script&family=Kalam:wght@700&family=Questrial&display=swap">
<style>
:root{
  --page:#efefef;
  --white:#ffffff;
  --green:#5bb500;
  --green-light:#8fd13a;
  --dark:#27221d;
  --dark-panel:#2b2520;
  --cream:#fdedcb;
  --tan:#8b7a5c;
  --tan-light:#d9c9a3;
  --text:#3a3530;
  --muted:#6d665e;
  --leaf-deep:#22361a;
  --leaf-mid:#3e5b2c;
}
*{box-sizing:border-box;margin:0;padding:0}
html,body{width:1200px;height:3680px;overflow:hidden}
body{background:var(--page);font-family:"Questrial",sans-serif;color:var(--text);position:relative}
.abs{position:absolute}
.script{font-family:"Kaushan Script",cursive}
.heading{font-family:"Kalam",cursive;font-weight:700}

/* header */
.site-header{left:20px;top:0;width:1160px;height:125px;background:var(--white)}
.brand{left:186px;top:32px;display:flex;align-items:center;gap:14px}
.brand-dot{width:34px;height:34px;border-radius:50%;background:var(--green)}
.brand-name{font-size:34px;color:var(--green);line-height:1}
.brand-tag{left:234px;top:78px;font-size:17px;color:var(--dark)}
.main-nav{left:492px;top:52px;display:flex;gap:16px;font-size:13px;color:var(--muted);letter-spacing:.5px}
.main-nav .active{color:var(--text)}
.nav-underline{left:492px;top:92px;width:44px;height:2px;background:var(--tan-light)}
.cart{left:880px;top:52px;font-size:13px;color:var(--muted)}
.cart-badge{left:977px;top:44px;width:16px;height:16px;background:var(--green)}

/* hero */
.hero{left:20px;top:125px;width:1160px;height:505px;background:radial-gradient(ellipse at 50% 40%,var(--leaf-mid),var(--leaf-deep) 75%)}
.hero-title{left:0;top:175px;width:1160px;text-align:center;font-size:58px;color:var(--green-light)}
.btn{display:flex;align-items:center;justify-content:center;letter-spacing:2px;text-transform:uppercase}
.btn-shop{left:448px;top:320px;width:267px;height:93px;background:var(--green);color:var(--white);font-size:22px;letter-spacing:1px}

/* feature tiles */
.tile{top:657px;width:232px;height:305px}
.tile-frame{position:absolute;inset:24px;border:2px solid var(--tan-light);display:flex;align-items:center;justify-content:center;text-align:center;font-size:13px;line-height:1.9;letter-spacing:1px;color:var(--white);font-weight:bold}
.tile-1{left:207px;background:linear-gradient(160deg,#b8a584,#8d7b5d)}
.tile-1 .tile-frame{color:#4a4030}
.tile-2{left:484px;background:linear-gradient(160deg,#2f2a1f,#1b1812)}
.tile-3{left:765px;background:linear-gradient(160deg,#4a3e2a,#2a2418)}

.welcome-title{left:0;top:972px;width:1200px;text-align:center;font-size:34px;color:var(--dark)}
.welcome-text{left:207px;top:1028px;width:790px;font-size:13.5px;line-height:24px;color:var(--muted)}
.btn-green{background:var(--green);color:var(--white);font-size:15px}
.btn-find{left:517px;top:1122px;width:169px;height:58px}

/* history */
.history{left:20px;top:1195px;width:1160px;height:430px;background:linear-gradient(90deg,#9d8a67,#c7b48f 50%,#9d8a67)}
.history-photo{left:174px;top:1195px;width:370px;height:430px;background:radial-gradient(circle at 50% 55%,#e9e6df 0,#8a8a73 45%,#3e3226 100%)}
.history-panel{left:564px;top:1195px;width:434px;height:430px;background:var(--dark-panel)}
.history-title{left:600px;top:1218px;font-size:30px;color:var(--tan-light)}
.history-tabs{left:600px;top:1275px;display:flex;gap:0;font-size:14px;color:var(--white);font-weight:bold}
.history-tabs span{width:64px;height:40px;display:flex;align-items:center;justify-content:center}
.history-tabs .current{background:var(--green)}
.history-box{left:605px;top:1328px;width:354px;height:175px;border:2px solid var(--green)}
.history-text{left:615px;top:1340px;width:185px;font-size:10.5px;line-height:19px;color:var(--tan-light)}
.history-thumb{left:812px;top:1340px;width:135px;height:150px;background:linear-gradient(160deg,#3a5a8a,#4f8a35)}

/* category */
.cat-title{left:0;top:1640px;width:1200px;text-align:center;font-size:34px;color:var(--dark)}
.cat-sub{left:0;top:1695px;width:1200px;text-align:center;font-size:26px;color:#8a7048}
.product{top:1759px;width:232px;height:245px;display:flex;align-items:center;justify-content:center;font-size:21px;color:var(--white)}
.product-fruit{left:207px;border-radius:50%;background:radial-gradient(circle,#d1c09a,#b39f78);color:#3a2e1c}
.product-mint{left:484px;background:linear-gradient(160deg,#5a1e26,#2a0e12)}
.product-treasure{left:765px;background:linear-gradient(160deg,#3a3525,#1c1a12)}
.price{top:2028px;width:232px;text-align:center;font-size:15px;color:var(--dark)}
.btn-cart{top:2061px;width:138px;height:54px;border:2px solid var(--tan);color:var(--tan);font-size:12px;letter-spacing:1.5px}
.btn-dark{background:var(--dark);color:var(--white);font-size:15px}
.btn-view{left:517px;top:2139px;width:169px;height:59px}

/* about */
.about{left:20px;top:2227px;width:1160px;height:308px;background:radial-gradient(ellipse at 40% 50%,#5a5550,#2c2a28 80%)}
.about-title{left:0;top:2275px;width:1200px;text-align:center;font-size:34px;color:var(--white)}
.about-text{left:370px;top:2340px;width:460px;text-align:center;font-size:15px;line-height:24px;color:#d8d6d2;letter-spacing:1px}
.btn-about{left:517px;top:2426px;width:169px;height:60px}

/* blog */
.blog{left:20px;top:2537px;width:1160px;height:427px;background:var(--cream)}
.blog-title{left:0;top:2550px;width:1200px;text-align:center;font-size:34px;color:var(--dark)}
.blog-sub{left:0;top:2596px;width:1200px;text-align:center;font-size:22px;color:#8a7048}
.blog-arrow{top:2680px;font-size:34px;color:var(--dark)}
.post-img{top:2636px;width:212px;height:144px}
.post-1{background:linear-gradient(160deg,#4b6a32,#8aa35c)}
.post-2{background:linear-gradient(160deg,#6a5a30,#a08c55)}
.post-3{background:linear-gradient(160deg,#b65a2a,#6a4a8a)}
.post-date{top:2790px;width:76px;height:29px;background:var(--dark);color:var(--white);font-size:10px;display:flex;align-items:center;justify-content:center;letter-spacing:1px}
.post-q{top:2830px;font-size:12px;color:var(--muted)}
.post-meta{top:2855px;width:212px;display:flex;justify-content:space-between;padding-right:60px;font-size:8.5px;color:var(--muted);letter-spacing:.5px}
.btn-blog{left:517px;top:2884px;width:169px;height:59px;background:#6d6150;color:var(--white);font-size:15px}

/* footer */
.footer{left:20px;top:2964px;width:1160px;height:173px;background:var(--dark)}
.footer-col{top:2964px;height:173px;text-align:center;color:var(--white)}
.footer-col h3{font-family:"Kalam",cursive;font-weight:700;font-size:19px;letter-spacing:1.5px;color:var(--tan-light);margin-top:40px;margin-bottom:22px}
.footer-col p{font-size:14px;line-height:22px}
.footer-divider{top:2984px;width:3px;height:133px;background:var(--white)}
.socials{display:flex;justify-content:center;gap:10px}
.socials span{width:28px;height:28px;border-radius:50%;background:var(--tan-light)}

.map{left:20px;top:3137px;width:1160px;height:463px;background:linear-gradient(135deg,#ecebe3,#e2e0d6 50%,#eceadf)}
.bottom-bar{left:20px;top:3600px;width:1160px;height:80px;background:var(--dark);color:var(--tan-light);font-size:17px;display:flex;align-items:center;justify-content:center}
</style>
</head>
<body>

<header class="abs site-header">
  <div class="abs brand"><span class="brand-dot"></span><span class="brand-name heading">Leafwell</span></div>
  <div class="abs brand-tag">Healthy with a heart</div>
  <nav class="abs main-nav"><span class="active">HOME</span><span>FEATURES</span><span>ABOUT</span><span>SHOP</span><span>BLOG</span><span>CONTACTS</span></nav>
  <div class="abs nav-underline"></div>
  <div class="abs cart">CART: 0 $0.00</div>
  <div class="abs cart-badge"></div>
</header>

<section class="abs hero" role="img" aria-label="Photo of a tea plantation with fresh green tea leaves">
  <h1 class="abs hero-title script">Each Tea is carefully blended</h1>
  <a class="abs btn btn-shop">SHOP NOW</a>
</section>

<div class="abs tile tile-1" role="img" aria-label="Photo of loose dried herbal tea"><div class="tile-frame">PERSONALISE<br>YOUR TEA</div></div>
<div class="abs tile tile-2" role="img" aria-label="Photo of dark loose leaf tea"><div class="tile-frame">VISIT OUR<br>STORE</div></div>
<div class="abs tile tile-3" role="img" aria-label="Photo of twisted black tea leaves"><div class="tile-frame">VISIT OUR<br>STORE</div></div>

<h2 class="abs welcome-title heading">Welcome</h2>
<p class="abs welcome-text">Each tea purchase comes with organically and ethically grown loose theleaf tea, carefully blended to create the perfect cup, where all the raw materials are being purchased from Indonesian local farmers in order to give them sustainable employment. Every 20% from the total amount of the customer's purchase from our website always goes back to their communities to help build better sanitation, education or whatever they need.</p>
<a class="abs btn btn-green btn-find">FIND OUT MORE</a>

<section class="abs history" role="img" aria-label="Textured background of scattered dried tea"></section>
<div class="abs history-photo" role="img" aria-label="Photo of a white bowl filled with green tea leaves"></div>
<div class="abs history-panel"></div>
<h2 class="abs history-title heading">History &amp; Awards</h2>
<div class="abs history-tabs"><span class="current">1990</span><span>2000</span><span>2010</span><span>2017</span></div>
<div class="abs history-box"></div>
<p class="abs history-text">Aliquam nec elit dignissim massa dignissim commodo non vestibulum ligula. Integer sed eros vel turpis aliquam. Aliquam nec elit dignissim massa dignissim commodo non vestibulum.</p>
<div class="abs history-thumb" role="img" aria-label="Photo of hands picking fresh tea leaves"></div>

<h2 class="abs cat-title heading">Category</h2>
<p class="abs cat-sub heading">Choose Your Health Secret</p>

<div class="abs product product-fruit heading" role="img" aria-label="Photo of Fruit Rhapsody tea blend">Fruit Rhapsody</div>
<div class="abs product product-mint heading" role="img" aria-label="Photo of Mint and Roses tea blend">Mint &amp; Roses</div>
<div class="abs product product-treasure heading" role="img" aria-label="Photo of Treasure Leaves tea blend">Treasure Leaves</div>

<p class="abs price" style="left:207px">$11.00</p>
<p class="abs price" style="left:484px">$16.00</p>
<p class="abs price" style="left:765px">$8.00</p>
<a class="abs btn btn-cart" style="left:254px">ADD TO CART</a>
<a class="abs btn btn-cart" style="left:531px">ADD TO CART</a>
<a class="abs btn btn-cart" style="left:812px">ADD TO CART</a>
<a class="abs btn btn-dark btn-view">VIEW MORE</a>

<section class="abs about" role="img" aria-label="Black and white photo of a hand holding soil"></section>
<h2 class="abs about-title heading">About Our Organization</h2>
<p class="abs about-text">Aliquam nec elit dignissim massa dignissim commodo non vestibulum ligula. Integer sed eros vel turpis aliquam mattis.</p>
<a class="abs btn btn-green btn-about">VIEW MORE</a>

<section class="abs blog"></section>
<h2 class="abs blog-title heading">Blog</h2>
<p class="abs blog-sub heading">Recent Articles</p>
<svg class="abs blog-arrow" style="left:205px;top:2695px" width="26" height="26" viewBox="0 0 26 26"><path d="M13 4 4 13l9 9M22 4l-9 9 9 9" fill="none" stroke="#27221d" stroke-width="2"/></svg>
<svg class="abs blog-arrow" style="left:970px;top:2695px" width="26" height="26" viewBox="0 0 26 26"><path d="M4 4l9 9-9 9M13 4l9 9-9 9" fill="none" stroke="#27221d" stroke-width="2"/></svg>

<div class="abs post-img post-1" style="left:240px" role="img" aria-label="Photo of dried green tea leaves"></div>
<div class="abs post-img post-2" style="left:494px" role="img" aria-label="Photo of loose golden tea"></div>
<div class="abs post-img post-3" style="left:747px" role="img" aria-label="Photo of colourful dried flower tea"></div>
<div class="abs post-date" style="left:240px">MAR 24</div>
<div class="abs post-date" style="left:494px">MAR 24</div>
<div class="abs post-date" style="left:747px">MAR 24</div>
<p class="abs post-q" style="left:240px">What team are you in:</p>
<p class="abs post-q" style="left:494px">What team are you in:</p>
<p class="abs post-q" style="left:747px">What team are you in:</p>
<div class="abs post-meta" style="left:240px"><span>BY ADMIN 0</span><span>COMMENTS</span></div>
<div class="abs post-meta" style="left:494px"><span>BY ADMIN 0</span><span>COMMENTS</span></div>
<div class="abs post-meta" style="left:747px"><span>BY ADMIN 0</span><span>COMMENTS</span></div>
<a class="abs btn btn-blog">GO TO BLOG</a>

<footer class="abs footer"></footer>
<div class="abs footer-col" style="left:185px;width:270px"><h3>ADDRESS</h3><p>48 Fernhill Road, Maple Grove,<br>IL 60521</p></div>
<div class="abs footer-divider" style="left:456px"></div>
<div class="abs footer-col" style="left:460px;width:280px"><h3>SOCIALS</h3><div class="socials"><span></span><span></span><span></span><span></span></div></div>
<div class="abs footer-divider" style="left:738px"></div>
<div class="abs footer-col" style="left:742px;width:270px"><h3>CONTACTS</h3><p>555-014-2290<br>hello@leafwell.example</p></div>

<div class="abs map" role="img" aria-label="Street map showing the shop location with a river and parks"></div>
<div class="abs bottom-bar">Your website © 2017 All Rights Reserved Terms of Use and Privacy Policy</div>

</body>
</html>
```